Flyer-Design für Vermittlung von Betreuungskräften
Zielgruppe
Wir vermitteln Betreuungskräfte aus Osteuropa für pflegebedürftige Menschen in Deutschland. Dabei legen wir Wert auf Seriösität, Professionalität und fürsorgliche Beratung. Folglich sind unsere Zielgruppe ältere Menschen und vor allem deren Angehörige, die für ihre Herzensmenschen entscheiden, ob die Pflege daheim ermöglicht wird. Der Flyer soll Wärme und Freundlichkeit ausstrahlen.
Aufgabenstellung
Es soll ein Wiedererkennungswert zu unserer Homepage sein. In den Flyer sollen folgende Kriterien:
-> Vorne: Schönes Bild von unserer HP, unser Slogan: Für Menschen. Aus Leidenschaft. und unser Logo
Weitere Inhalte/Seiten:
-> Kontakt mit Bild der jew. Ansprechpartner: Ich freue mich auf Ihre Kontaktaufnahme!
-> über uns mit folgendem Text:
'Wenn ein Mensch im Familien- oder Bekanntenkreis pflegebedürftig wird, stehen Angehörige meist vor einer großen Herausforderung und vielen Fragen. Wir sind Ihr Ansprechpartner und haben das Anliegen, pflegebedürftigen Menschen mit einer osteuropäischen liebevollen Betreuungskraft den Verbleib im eigenen Zuhause zu ermöglichen. '
-> Aufgaben der Betreuungskraft
- Grundpflege
Hilfe bei der Körperpflege, An- und auskleiden, Toilettengänge, Unterstützung beim Aufstehen usw.
- Haushaltshilfe
Aufräumen, Staubsaugen, Wäsche waschen, Geschirr spülen und mehr
- Kochen und Ernährung
sorgt sich um das leibliche Wohl inkl. Einhaltung Ernährungspläne, einkaufen von Lebensmitteln
- soziale Betreuung
Schutz vor Vereinsamung, spazieren gehen, Ausflüge, Pflege von Hobbies, Begleitung bei Arztbesuchen
Gerne mit schönen Symbolen
-> Warum belanoxa? siehe Homepage anlehnend an: Sechs Gründe, die für uns sprechen
-> Vier Schritte zu Ihrer Betreuungskraft siehe Homepage
Schrift Trenda
www.belanoxa,de

```html
<!DOCTYPE html>
<html lang="de">
<head>
<meta charset="utf-8">
<title>belanoxa – Flyer</title>
<link rel="stylesheet" href="https://fonts.googleapis.com/css2?family=Didact+Gothic&family=Cookie&display=swap">
<style>
  :root{
    --bg:#f8e2e5;
    --panel:#ffffff;
    --red:#d3222c;
    --arc:#e07f89;
    --text:#5a5a5a;
    --dark:#4a4a4a;
    --body-font:"Didact Gothic", "Century Gothic", sans-serif;
    --script-font:"Cookie", cursive;
  }
  *{box-sizing:border-box;margin:0;padding:0}
  html,body{width:1200px;height:813px;overflow:hidden;background:var(--bg)}
  .flyer{position:relative;width:1200px;height:813px;overflow:hidden;background:var(--bg);font-family:var(--body-font);color:var(--text)}
  .arc{position:absolute;left:0;top:0}
  .card{position:absolute;background:var(--panel);border-radius:16px;overflow:hidden}
  .title{display:flex;align-items:center;justify-content:center;font-family:var(--script-font);color:var(--dark);font-size:48px;line-height:1;white-space:nowrap}
  .subhead{position:absolute;left:0;right:0;top:12px;text-align:center;font-family:var(--script-font);font-weight:400;color:var(--red);font-size:26px;line-height:1.1;white-space:nowrap}
  .item{position:absolute;font-size:13.5px;line-height:17.6px;letter-spacing:-0.2px;hyphens:auto;-webkit-hyphens:auto}
  .item .num{position:absolute;left:-21px;top:0;color:var(--red)}
  .item .label{color:var(--red);text-decoration:underline;text-underline-offset:2px;text-decoration-thickness:1px}
  .left .item{left:27px;width:292px}
  .middle .item{left:28px;width:292px}
  .brand{display:flex;align-items:center;justify-content:center;gap:14px}
  .brand-dot{width:40px;height:40px;border-radius:50%;background:var(--red)}
  .brand-name{font-size:40px;color:var(--red);line-height:1}
  .photo{position:absolute;left:16px;top:16px;width:279px;height:198px;border-radius:12px;
    background:linear-gradient(100deg,#d9cfc8 0%,#efe4e2 35%,#c9a591 60%,#9fd6c8 100%)}
  .slogan-line1{position:absolute;left:14px;top:250px;font-size:41px;line-height:1;color:var(--dark);white-space:nowrap}
  .slogan-line2{position:absolute;left:16px;top:302px;font-family:var(--script-font);font-size:56px;line-height:1;color:var(--dark);white-space:nowrap}
  .contact-title{position:absolute;left:0;right:0;top:12px;text-align:center;font-family:var(--script-font);font-weight:400;font-size:26px;line-height:1;color:var(--dark)}
  .contact-row{position:absolute;left:16px;display:flex;align-items:flex-start}
  .contact-row svg{width:40px;height:40px;flex:none;margin-right:14px}
  .contact-row .label{color:var(--red);text-decoration:underline;text-underline-offset:2px;font-size:16px;line-height:19px}
  .contact-row .value{font-size:16px;line-height:20px;color:var(--text);white-space:nowrap}
</style>
</head>
<body>
<div class="flyer">
  <svg class="arc" width="1200" height="813" viewBox="0 0 1200 813" aria-hidden="true">
    <circle cx="170" cy="330" r="424" fill="none" stroke="var(--arc)" stroke-width="6"/>
  </svg>

  <div class="card title" style="left:49px;top:49px;width:319px;height:82px">Ihre Betreuungskraft</div>
  <section class="card left" style="left:49px;top:161px;width:325px;height:602px">
    <h2 class="subhead">Vier Schritte zu Ihrer Betreuungskraft</h2>
    <div class="item" style="top:58px"><span class="num">1.</span><span class="label">Ihre Anfrage</span><br>Sie beschreiben uns die Situation und schildern uns Ihre Wünsche an die osteuropäische Pflegekraft.</div>
    <div class="item" style="top:163px"><span class="num">2.</span><span class="label">Angebot</span><br>Wir prüfen gemeinsam Ihren Bedarf und erstellen Ihnen anschließend ein persönliches Angebot.</div>
    <div class="item" style="top:251px"><span class="num">3.</span><span class="label">Personalvorschläge</span><br>Sie wählen die für Sie passende Betreuungskraft aus und entscheiden sich für eine Zusammenarbeit mit uns.</div>
    <div class="item" style="top:338px"><span class="num">4.</span><span class="label">Ihre Pflegekraft</span><br>Die 24-Stunden-Pflege beginnt die Betreuung zum gewünschten Zeitpunkt.</div>
  </section>

  <div class="card title" style="left:444px;top:49px;width:319px;height:82px">Warum belanoxa?</div>
  <section class="card middle" style="left:437px;top:161px;width:325px;height:602px">
    <h2 class="subhead">Sechs Gründe, die für uns sprechen.</h2>
    <div class="item" style="top:48px"><span class="num">1.</span><span class="label">Hoher Qualitätsstandard und Partnerauswahl</span><br>Wir haben hohe Ansprüche an uns selbst – und diese haben wir auch an unsere Partner in Osteuropa. Wir arbeiten nur mit seriösen und transparenten Anbietern zusammen.</div>
    <div class="item" style="top:153px"><span class="num">2.</span><span class="label">Geprüfte Personalvorschläge</span><br>Sie erhalten nur Personalvorschläge von Betreuungskräften, die zu Ihnen und Ihrer Situation passen.</div>
    <div class="item" style="top:240px"><span class="num">3.</span><span class="label">Individuelle Beratung</span><br>Wir erarbeiten eine auf Ihre Situation angepasste Lösung, die sowohl für den Pflegebedürftigen als auch für die Angehörigen stimmig ist.</div>
    <div class="item" style="top:328px"><span class="num">4.</span><span class="label">Transparenz</span><br>Transparenz ist in diesem sensiblen Tätigkeitsfeld unerlässlich. Wir beraten Sie ehrlich, loyal und auf höchstem Standard.</div>
    <div class="item" style="top:416px"><span class="num">5.</span><span class="label">Realistische Preisgestaltung</span><br>Wir garantieren, dass Sie bei uns immer hohe Leistungen zu fairen Preisen bekommen.</div>
    <div class="item" style="top:486px"><span class="num">6.</span><span class="label">Begleitete Anreise</span><br>Damit sich alle Parteien wohlfühlen, bieten wir optional ein Kennenlernen sowie eine Einführung vor Ort an, damit sich jeder von Anfang an wohl fühlt.</div>
  </section>

  <div class="card brand" style="left:839px;top:49px;width:311px;height:81px">
    <span class="brand-dot"></span>
    <span class="brand-name">belanoxa</span>
  </div>
  <section class="card" style="left:839px;top:160px;width:311px;height:391px">
    <div class="photo" role="img" aria-label="Foto: ältere Dame und Betreuungskraft lehnen liebevoll die Köpfe aneinander"></div>
    <p class="slogan-line1">Für Menschen.</p>
    <p class="slogan-line2">Aus Leidenschaft.</p>
  </section>
  <section class="card" style="left:839px;top:576px;width:311px;height:186px">
    <h2 class="contact-title">Kontakt</h2>
    <div class="contact-row" style="top:50px">
      <svg viewBox="0 0 40 40" aria-hidden="true"><path d="M8 4c3-2 5-1 6 1l3 6c1 2 0 3-2 4l-2 1c2 5 6 9 11 11l1-2c1-2 2-3 4-2l6 3c2 1 3 3 1 6-2 3-5 4-8 3C17 32 8 23 5 13 4 9 5 6 8 4z" fill="none" stroke="var(--red)" stroke-width="2" stroke-linejoin="round"/></svg>
      <div><div class="label">Telefon</div><div class="value">07431 / 48 20 519</div></div>
    </div>
    <div class="contact-row" style="top:95px">
      <svg viewBox="0 0 40 40" aria-hidden="true"><rect x="2" y="9" width="36" height="24" fill="none" stroke="var(--red)" stroke-width="2"/><path d="M2 9l18 14 18-14M2 33l13-13M38 33L25 20" fill="none" stroke="var(--red)" stroke-width="2"/></svg>
      <div><div class="label">Kundenservice</div><div class="value">info@belanoxa.de</div></div>
    </div>
    <div class="contact-row" style="top:140px">
      <svg viewBox="0 0 40 40" aria-hidden="true"><path d="M20 38C14 29 8 22 8 15a12 12 0 0 1 24 0c0 7-6 14-12 23z" fill="none" stroke="var(--red)" stroke-width="2"/><circle cx="20" cy="15" r="4" fill="none" stroke="var(--red)" stroke-width="2"/></svg>
      <div><div class="label">Adresse</div><div class="value">Lindenweg 12 &nbsp;|&nbsp; 72458 Albstadt</div></div>
    </div>
  </section>
</div>
</body>
</html>
```